IT services company needs a business card designed

-2 sided business card.-Front is going to be the logo raised (3D floating effect) on a black background. Make the logos spider web shiny silver and keep the spider the same design. -Back needs to have the following information:Darrel Sotho, Managing Partner, Cell: 738-402-1954, Website: Plankhorn.com, Email: Darrel@Plankhorn.com
Target Market(s)
IT Services
Industry/Entity Type
It Company
Contact Information for Business Card
-2 sided business card.
-Front is going to be the logo raised (3D floating effect) on a black background. Make the logos spider web shiny silver and keep the spider the same design.
-Back needs to have the following information:
Darrel Sotho, Managing Partner, Cell: 738-402-1954, Website: Plankhorn.com, Email: Darrel@Plankhorn.com

```html
<!DOCTYPE html>
<html lang="en">
<head>
<meta charset="utf-8">
<title>Plankhorn Business Card</title>
<link rel="stylesheet" href="https://fonts.googleapis.com/css2?family=Roboto:wght@300;400;500&display=swap">
<style>
  :root {
    --page: #ffffff;
    --card: #000000;
    --ink: #ffffff;
    --ink-soft: #e6e6e6;
    --accent: #3fa9e8;
  }
  * { margin: 0; padding: 0; box-sizing: border-box; }
  html, body {
    width: 886px;
    height: 1200px;
    overflow: hidden;
    background: var(--page);
    font-family: "Roboto", Arial, sans-serif;
  }
  .canvas {
    position: relative;
    width: 886px;
    height: 1200px;
  }
  .card {
    position: absolute;
    left: 0;
    width: 886px;
    background: var(--card);
    color: var(--ink);
  }
  .card--front { top: 13px; height: 570px; }
  .card--back { top: 606px; height: 572px; }

  .brand {
    position: absolute;
    left: 0;
    right: 0;
    top: 250px;
    display: flex;
    align-items: center;
    justify-content: center;
    gap: 22px;
  }
  .brand__name {
    font-weight: 300;
    font-size: 70px;
    letter-spacing: 6px;
    color: var(--ink);
    line-height: 1;
  }
  .brand__dot {
    width: 16px;
    height: 16px;
    border-radius: 50%;
    background: var(--accent);
  }

  .contact {
    position: absolute;
    left: 79px;
    top: 92px;
  }
  .contact__name {
    display: inline-block;
    font-weight: 500;
    font-size: 84px;
    line-height: 1;
    letter-spacing: 1px;
    padding-bottom: 22px;
    border-bottom: 5px solid var(--ink);
  }
  .contact__role {
    margin-top: 40px;
    font-weight: 400;
    font-size: 42px;
    line-height: 1;
  }
  .contact__list {
    list-style: none;
    margin-top: 26px;
    font-weight: 300;
    font-size: 32px;
    line-height: 45px;
    color: var(--ink-soft);
  }
</style>
</head>
<body>
<main class="canvas">
  <section class="card card--front" aria-label="Card front">
    <div class="brand">
      <span class="brand__name">PLANKHORN</span>
      <span class="brand__dot"></span>
    </div>
  </section>

  <section class="card card--back" aria-label="Card back">
    <div class="contact">
      <h1 class="contact__name">DARREL SOTHO</h1>
      <p class="contact__role">Managing Partner</p>
      <ul class="contact__list">
        <li>Cell: 738-402-1954</li>
        <li>Website: Plankhorn.com</li>
        <li>Email: Darrel@Plankhorn.com</li>
      </ul>
    </div>
  </section>
</main>
</body>
</html>
```